Flyer-Design für Basilikum frisch-gruen-kochen-schlemmen
Zielgruppe
Hallo wir brauchen wieder Flyer für unser Lokal in Frankfurt. Es soll jetzt nichts besonderes beworben werden, also 'nur' Info wie das es uns gibt, wo wir zu finden sind, Kontaktdaten, Öffnungszeiten etc. Gedacht sind die Flyer quasi als Imageflyer.
Aufgabenstellung
Wir haben schonmal Flyer verwendet die ich selbst gestaltet habe, jetzt soll etwas neues, zeitgemässes her.
Göße: A6

```html
<!DOCTYPE html>
<html lang="de">
<head>
<meta charset="utf-8">
<title>Basilikum – Flyer</title>
<link href="https://fonts.googleapis.com/css2?family=Barlow+Condensed:wght@700&family=Barlow:wght@700&family=Open+Sans:wght@700&display=swap" rel="stylesheet">
<style>
  :root {
    --stage: #d9d9d9;
    --brand-red: #a31f1f;
    --band-red: #7f1510;
    --leaf-green: #5f8a4e;
    --paper: #f6f6f2;
    --white: #ffffff;
  }
  * { box-sizing: border-box; margin: 0; padding: 0; }
  html, body {
    width: 1200px; height: 900px; overflow: hidden;
    background: var(--stage);
  }
  .flyer {
    position: absolute; left: 310px; top: 40px;
    width: 580px; height: 820px;
    background: var(--paper);
    overflow: hidden;
    box-shadow: 0 4px 14px rgba(0,0,0,.18);
  }
  .flyer__photo {
    position: absolute; inset: 0;
    background:
      radial-gradient(ellipse 45% 14% at 52% 48%, rgba(230,120,70,.75), transparent 70%),
      radial-gradient(ellipse 30% 10% at 40% 73%, rgba(225,100,55,.7), transparent 70%),
      radial-gradient(ellipse 40% 18% at 70% 85%, rgba(235,225,205,.8), transparent 70%),
      linear-gradient(180deg, #f7f8f3 0%, #eef1e6 10%, #c7d6b4 30%, #9fbf86 50%, #86aa6c 70%, #a4bb8c 88%, #c9cfb8 100%);
  }
  .brand {
    position: absolute; left: 0; right: 0; top: 80px;
    display: flex; align-items: center; justify-content: center; gap: 18px;
  }
  .brand__name {
    font-family: "Barlow Condensed", sans-serif;
    font-weight: 700; font-size: 112px; line-height: 1;
    color: var(--brand-red); letter-spacing: 1px;
  }
  .brand__mark {
    width: 58px; height: 58px; background: var(--leaf-green); border-radius: 8px;
  }
  .tagline {
    position: absolute; left: 0; right: 0; top: 250px;
    display: flex; justify-content: center; align-items: center; gap: 9px;
    font-family: "Open Sans", sans-serif; font-weight: 700;
    font-size: 19px; letter-spacing: 2.5px; color: var(--brand-red);
  }
  .tagline__dot { width: 8px; height: 8px; background: var(--leaf-green); }
  .claim {
    position: absolute; left: 0; right: 0; top: 420px; height: 124px;
    background: var(--band-red);
    border-top: 2px solid var(--white); border-bottom: 2px solid var(--white);
    padding: 16px 0 0 34px;
    font-family: "Barlow", sans-serif; font-weight: 700;
    font-size: 42px; line-height: 50px; color: var(--white);
  }
</style>
</head>
<body>
  <main class="flyer">
    <div class="flyer__photo" role="img" aria-label="Foto eines frischen Salats mit Rucola, Tomaten und Oliven, weich unscharf"></div>
    <div class="brand">
      <span class="brand__name">BASILIKUM</span>
      <span class="brand__mark"></span>
    </div>
    <div class="tagline">
      <span>FRISCH</span><span class="tagline__dot"></span>
      <span>GRUEN</span><span class="tagline__dot"></span>
      <span>KOCHEN</span><span class="tagline__dot"></span>
      <span>SCHLEMMEN</span>
    </div>
    <h1 class="claim">Frankfurt´s erstes<br>Vegan Restaurant</h1>
  </main>
</body>
</html>
```